Book and Ebook Cover for my Upcoming Book

About the Book
------------------
I need a book, ebook and if possible audio cover design for my upcoming book - Lanterns & Tides. This is my first book and really looking for a great book cover. The book is about my story, living with Mental Health and how to reclaim control of your life.

Pressmarble
-----------
I am using pressmarble.example to self-publish my book so in case of any design-related questions you can just search info on their website.

I have an initial theme I am thinking for the design book cover which I have attached. You can use this as a starting point.

Idea for the theme
---------------------
I am thinking about a phoenix to represent rising from the ashes and rebirth. The phoenix motif will be continued throughout the interior pages of the book. I'd like the cover of the book to be minimal, white with gold lettering, and maybe incorporating wings? feel free to play around with the idea and up for suggestions.

If you can think of something along these lines and make it a lot better that would be great.

What I need
---------------
The book is complete and is Trim size is 6.14 x 9.21” (234 x 156mm). I would need-
1. Book Cover
2. Back & Spine Design
3. Source File
4. Ebook Cover
5. Need multiple revisions to get the best possible outcome
6. My name and book title should also on the front cover
7. The book title should be bigger size than the subtitle

If you can give me Audiobook cover, I would love that as well and can pay extra for it if needed.

I love this for the interior phoenix motif:
https://artbazaarhub.example/VelloStudioWorks/7720418-Painted-Firebird-Graphic-Pack#fullscreen

The only other actual book cover I found online that remotely relates to what I am looking for is this -
https://www.searchloop.example/url?sa=i&url=https%3A%2F%2Fshotgallery.example%2Fkorvath&psig=BxQmTr7LK2pNvW4ZsYeHd83QaPLJ&ust=1598415525610000&source=images&cd=vfe&ved=1HXdkRmQBvubDGrTLkxbWsTqYhpTGEgcDHRRRRRHdBBBBBBCE

Target Market(s)

Personal Development
Mental health

Requirements
Must have
• 1. Book Cover
2. Back & Spine Design
3. Source File
4. Ebook Cover
Nice to have
• Audiobook cover as I eventually will be releasing the audio version of the book

```html
<!DOCTYPE html>
<html lang="en">
<head>
<meta charset="utf-8">
<title>Lanterns &amp; Tides — Cover Spread</title>
<link rel="stylesheet" href="https://fonts.googleapis.com/css2?family=Macondo+Swash+Caps&family=Marcellus&display=swap">
<style>
  :root {
    --band-grey: #e3e3e3;
    --paper: #ffffff;
    --ink: #1c1a1a;
    --ink-soft: #2a2727;
    --feather-gold: #c8903f;
    --feather-rose: #d07a5c;
    --feather-cream: #f6e6d8;
    --title-font: "Macondo Swash Caps", fantasy;
    --body-font: "Marcellus", serif;
  }
  html, body {
    margin: 0;
    padding: 0;
    width: 1200px;
    height: 1000px;
    overflow: hidden;
    background: var(--paper);
  }
  .spread {
    position: relative;
    width: 1200px;
    height: 1000px;
    background: var(--paper);
    color: var(--ink);
  }
  .band {
    position: absolute;
    left: 0;
    width: 1200px;
    background: var(--band-grey);
  }
  .band--top { top: 0; height: 73px; }
  .band--bottom { top: 927px; height: 73px; }

  /* Back cover */
  .back-heading {
    position: absolute;
    left: 57px;
    width: 477px;
    top: 138px;
    margin: 0;
    text-align: center;
    font-family: var(--title-font);
    font-weight: 400;
    font-size: 38px;
    letter-spacing: 3px;
    text-transform: uppercase;
  }
  .back-tagline {
    position: absolute;
    left: 57px;
    width: 477px;
    top: 222px;
    margin: 0;
    text-align: center;
    font-family: var(--body-font);
    font-size: 21px;
    text-decoration: underline;
    text-underline-offset: 3px;
    text-decoration-thickness: 1px;
  }
  .blurb {
    position: absolute;
    left: 57px;
    width: 480px;
    margin: 0;
    font-family: var(--body-font);
    font-size: 15.2px;
    line-height: 18.5px;
    color: var(--ink-soft);
  }
  .blurb--1 { top: 321px; }
  .blurb--2 { top: 413px; }
  .blurb--3 { top: 505px; }
  .blurb--4 { top: 634px; }

  /* Spine */
  .spine-text {
    position: absolute;
    left: 599px;
    margin: 0;
    font-family: var(--title-font);
    font-weight: 400;
    font-size: 24px;
    letter-spacing: 3px;
    white-space: nowrap;
    text-transform: uppercase;
    transform-origin: left top;
    transform: rotate(90deg) translateY(-50%);
  }
  .spine-title { top: 203px; }
  .spine-author { top: 586px; }

  /* Front cover */
  .front-subtitle {
    position: absolute;
    left: 660px;
    width: 496px;
    top: 110px;
    margin: 0;
    text-align: center;
    font-family: var(--title-font);
    font-size: 16.5px;
    line-height: 22px;
    letter-spacing: 1px;
    text-transform: uppercase;
  }
  .wings-art {
    position: absolute;
    left: 663px;
    top: 154px;
    width: 491px;
    height: 412px;
    background:
      radial-gradient(ellipse 30% 55% at 22% 50%, var(--feather-rose) 0%, var(--feather-gold) 45%, rgba(255,255,255,0) 100%),
      radial-gradient(ellipse 30% 55% at 78% 50%, var(--feather-rose) 0%, var(--feather-gold) 45%, rgba(255,255,255,0) 100%),
      radial-gradient(ellipse 40% 20% at 50% 88%, var(--feather-cream) 0%, rgba(255,255,255,0) 100%);
    opacity: 0.85;
  }
  .front-title {
    position: absolute;
    left: 660px;
    width: 496px;
    top: 570px;
    margin: 0;
    text-align: center;
    font-family: var(--title-font);
    font-weight: 400;
    font-size: 64px;
    line-height: 67px;
    letter-spacing: 7px;
    text-transform: uppercase;
    text-shadow: 1px 2px 3px rgba(0,0,0,0.35);
  }
  .front-title span { display: block; }
  .front-author {
    position: absolute;
    left: 660px;
    width: 496px;
    top: 816px;
    margin: 0;
    text-align: center;
    font-family: var(--title-font);
    font-size: 27px;
    letter-spacing: 3px;
    text-transform: uppercase;
  }
</style>
</head>
<body>
<main class="spread">
  <div class="band band--top"></div>
  <div class="band band--bottom"></div>

  <section class="back-cover">
    <h2 class="back-heading">A Story of Hope</h2>
    <p class="back-tagline">When Struggle Leads to Empowerment</p>
    <p class="blurb blurb--1">Lorem ipsum dolor sit amet, consectetur adipiscing elit, sed do eiusmod tempor incididunt ut labore et dolore magna aliqua. Quis ipsum suspendisse ultrices gravida. Risus commodo viverra mae­cenas accumsan lacus vel facilisis.</p>
    <p class="blurb blurb--2">Lorem ipsum dolor sit amet, consectetur adipiscing elit, sed do eiusmod tempor incididunt ut labore et dolore magna aliqua. Quis ipsum suspendisse ultrices gravida. Risus commodo viverra mae­cenas accumsan lacus vel facilisis.</p>
    <p class="blurb blurb--3">Lorem ipsum dolor sit amet, consectetur adipiscing elit, sed do eiusmod tempor incididunt ut labore et dolore magna aliqua. Quis ipsum suspendisse ultrices gravida. Risus commodo viverra mae­cenas accumsan lacus vel facilisis.</p>
    <p class="blurb blurb--4">Lorem ipsum dolor sit amet, consectetur adipiscing elit, sed do eiusmod tempor incididunt ut labore et dolore magna aliqua. Quis ipsum suspendisse ultrices gravida. Risus commodo viverra mae­cenas accumsan lacus vel facilisis.</p>
  </section>

  <section class="spine">
    <p class="spine-text spine-title">Lanterns &amp; Tides</p>
    <p class="spine-text spine-author">Mirela Task</p>
  </section>

  <section class="front-cover">
    <p class="front-subtitle">Manage your mental health, reinvent your life<br>and ultimately own your story</p>
    <div class="wings-art" role="img" aria-label="Painted phoenix feathers arranged as a pair of rising wings in rose, gold and cream"></div>
    <h1 class="front-title"><span>Lanterns</span><span>&amp;</span><span>Tides</span></h1>
    <p class="front-author">Mirela Task</p>
  </section>
</main>
</body>
</html>
```